Mobile Fitness snd Therapy Business Card Design

I need a business card designed for my mobile fitness and therapy business.

Please view the images that I have uploaded. I like the simplicity of the design that I have attached. I adapted it with my information

Target Market(s)

Those seeking personal training, injury rehabilitation or massage therapy.

Industry/Entity Type

Business

Contact Information for Business Card

Dylan Marwick - MSc, CAT(C), RMT, CSCS, Pn2
e-mail: dylan@vantrelo.com
website: www.vantrelo.com
instagram: @dylan_marwick

Font styles to use
Sans Serif

Colors
3176b5
0355a3

Requirements
Must have
• "Contact us to receive a FREE assessment"
• Services offered:
• Personal Training
• Golf Fitness
• Injury Rehab
• Massage Therapy
• Yoga
Nice to have
• Consistent colours with brand
• - Dark Blue: #232837
• - Blue: #5096f0
• Consistent look/feel with the website: www.vantrelo.com

```html
<!DOCTYPE html>
<html lang="en">
<head>
<meta charset="utf-8">
<title>Vantrelo Business Card</title>
<link href="https://fonts.googleapis.com/css2?family=Roboto:wght@400;500;700&display=swap" rel="stylesheet">
<style>
  :root {
    --backdrop: #e9e9ec;
    --card: #0c0c0e;
    --card-edge: #1b1b1f;
    --blue: #5096f0;
    --blue-deep: #3176b5;
    --white: #f2f2f2;
    --grey: #cfcfcf;
    --divider: #3a3a40;
  }
  * { box-sizing: border-box; margin: 0; padding: 0; }
  html, body {
    width: 1200px; height: 900px; overflow: hidden;
    background: var(--backdrop);
    font-family: "Roboto", Arial, sans-serif;
  }
  .stage {
    width: 1200px; height: 900px;
    display: flex; align-items: center; justify-content: center; gap: 40px;
  }
  .card {
    position: relative;
    width: 540px; height: 308px;
    background: var(--card);
    border: 1px solid var(--card-edge);
    box-shadow: 0 14px 30px rgba(0,0,0,.25);
    color: var(--white);
  }
  .divider {
    position: absolute; width: 1px; background: var(--divider);
  }

  /* Front */
  .brand {
    position: absolute; left: 40px; bottom: 62px;
  }
  .brand-name {
    display: flex; align-items: center; gap: 8px;
    font-size: 34px; font-weight: 500; letter-spacing: 3px; color: var(--white);
  }
  .brand-mark { width: 14px; height: 14px; background: var(--blue); }
  .brand-tagline {
    margin-top: 4px; font-size: 10.5px; font-weight: 700; letter-spacing: 1.6px; color: var(--white);
  }
  .front .divider { left: 282px; top: 60px; height: 150px; }
  .contact { position: absolute; left: 302px; top: 62px; }
  .contact-name {
    font-size: 21px; font-weight: 700; color: var(--blue); letter-spacing: .3px;
  }
  .contact-creds { font-size: 13.5px; color: var(--grey); margin-top: 2px; }
  .contact-list { list-style: none; margin-top: 12px; }
  .contact-list li {
    display: flex; align-items: center; gap: 8px;
    font-size: 13.5px; color: var(--grey); margin-bottom: 6px;
  }
  .contact-list svg { width: 14px; height: 14px; flex: none; }

  /* Back */
  .feature {
    position: absolute; left: 40px; top: 70px; width: 230px; height: 130px;
    display: flex; align-items: center; justify-content: center;
    font-size: 34px; font-weight: 500; letter-spacing: 3px; color: #c9c9cc;
  }
  .back .divider { left: 292px; top: 40px; height: 160px; }
  .services { position: absolute; left: 312px; top: 48px; }
  .services-title {
    font-size: 14px; font-weight: 700; color: var(--blue); letter-spacing: .3px;
  }
  .services-list { list-style: none; margin-top: 8px; }
  .services-list li {
    display: flex; align-items: center; gap: 8px;
    font-size: 12px; color: var(--grey); margin-bottom: 4px; text-transform: uppercase;
  }
  .services-list li::before {
    content: ""; width: 7px; height: 7px; background: var(--blue-deep);
  }
  .cta {
    position: absolute; left: 0; right: 0; bottom: 40px; text-align: center;
    font-size: 12.5px; font-weight: 700; color: var(--blue-deep); letter-spacing: .5px;
  }
</style>
</head>
<body>
<main class="stage">
  <section class="card front">
    <div class="brand">
      <div class="brand-name"><span>VANTRELO</span><span class="brand-mark"></span></div>
      <div class="brand-tagline">NUTRITION - FITNESS - HEALTH</div>
    </div>
    <div class="divider"></div>
    <div class="contact">
      <h1 class="contact-name">DYLAN MARWICK</h1>
      <p class="contact-creds">MSc, CAT(C), RMT, CSCS, Pn2</p>
      <ul class="contact-list">
        <li>
          <svg viewBox="0 0 14 14"><rect x="1" y="3" width="12" height="8" fill="#5096f0"/><path d="M1 3 L7 8 L13 3" stroke="#0c0c0e" stroke-width="1.2" fill="none"/></svg>
          dylan@vantrelo.com
        </li>
        <li>
          <svg viewBox="0 0 14 14"><circle cx="7" cy="7" r="6" fill="#5096f0"/><path d="M1 7 H13 M7 1 C4 4 4 10 7 13 M7 1 C10 4 10 10 7 13" stroke="#0c0c0e" stroke-width="1" fill="none"/></svg>
          www.vantrelo.com
        </li>
        <li>
          <svg viewBox="0 0 14 14"><rect x="1" y="1" width="12" height="12" fill="#5096f0"/></svg>
          @dylan_marwick
        </li>
      </ul>
    </div>
  </section>

  <section class="card back">
    <div class="feature">VANTRELO</div>
    <div class="divider"></div>
    <div class="services">
      <h2 class="services-title">SERVICES OFFERED:</h2>
      <ul class="services-list">
        <li>Personal Training</li>
        <li>Golf Fitness</li>
        <li>Injury Rehab</li>
        <li>Massage Therapy</li>
        <li>Yoga</li>
      </ul>
    </div>
    <p class="cta">CONTACT US TO RECEIVE A FREE ASSESSMENT</p>
  </section>
</main>
</body>
</html>
```